Glossport Drag

The site will showcase the different drag queens of Manchester and provide an area for photography, video, social media feeds (such as flonker and Vombleth) as well as reviews of Drag queens to give the public a place to discuss shows or individuals.

Target Market(s)

Gay men

Industry/Entity Type

Media

Font styles to use
Decorative

Colors

Designer to choose colors to be used in the design.

Requirements
Must have
• Bright, bold, showbiz, glamorous but a little tacky at the same time.

```html
<!DOCTYPE html>
<html lang="en">
<head>
<meta charset="utf-8">
<title>Glossport Drag</title>
<link rel="stylesheet" href="https://fonts.googleapis.com/css2?family=Hind:wght@300;400;500;600&family=Open+Sans:wght@400;600;700&display=swap">
<style>
:root{
  --black:#000;
  --purple:#a21fc4;
  --purple-dark:#7e149b;
  --purple-text:#7b1a9a;
  --hero-bg:#252b45;
  --gold:#e2a41c;
  --orange:#e8951b;
  --grey-text:#6a6a6a;
  --light-text:#8a8a8a;
  --panel:#f7f7f7;
  --line:#e3e3e3;
  --fb-blue:#3a63a8;
  --tw-cyan:#2ac0e4;
  --link-cyan:#28a9d6;
  --footer:#262626;
}
*{margin:0;padding:0;box-sizing:border-box}
html,body{width:823px;height:1200px;overflow:hidden;background:#fff}
body{position:relative;font-family:"Open Sans",Arial,sans-serif;color:var(--grey-text)}
.abs{position:absolute}
.head-font{font-family:"Hind",Arial,sans-serif}

.site-header{left:0;top:0;width:823px;height:80px;background:var(--black)}
.brand{left:302px;top:30px;display:flex;align-items:center;gap:6px;color:#fff;font-family:"Hind",sans-serif;font-size:24px;font-weight:500}
.brand-mark{width:16px;height:16px;border-radius:50%;background:var(--purple)}
.social{left:636px;top:53px;display:flex;gap:3px}
.social span{width:16px;height:16px;border-radius:50%;background:#fff}

.main-nav{left:0;top:80px;width:823px;height:32px;background:linear-gradient(var(--purple),var(--purple-dark))}
.main-nav ul{list-style:none;display:flex;position:absolute;left:131px;top:0;height:32px}
.main-nav li{height:32px;line-height:33px;color:#fff;font-family:"Hind",sans-serif;font-weight:600;font-size:11px;padding:0 16px;border-left:1px solid rgba(255,255,255,.25)}
.main-nav li:first-child{border-left:none}

.hero{left:0;top:112px;width:823px;height:302px;background:var(--hero-bg)}
.hero-photo{left:364px;top:112px;width:372px;height:302px;background:radial-gradient(circle at 55% 40%,#c79a8a 0,#8a4fa8 35%,#3c2f6a 75%,#262a48 100%)}
.hero-title{left:120px;top:186px;color:#fff;font-family:"Hind",sans-serif;font-size:27px;font-weight:500}
.hero-sub{left:121px;top:220px;color:#fff;font-family:"Hind",sans-serif;font-size:15px;font-weight:300}
.hero-text{left:122px;top:245px;width:240px;color:#8b8fa8;font-size:7.6px;line-height:13px}
.dots{left:122px;top:291px;display:flex;gap:2px}
.dots span{width:8px;height:8px;border-radius:50%;background:#fff}

.intro-title{left:121px;top:458px;color:var(--purple-text);font-family:"Hind",sans-serif;font-size:18.5px;font-weight:500}
.intro-sub{left:122px;top:483px;color:#777;font-family:"Hind",sans-serif;font-size:10px;font-weight:400}
.intro-text{left:122px;top:502px;width:330px;font-size:7.4px;line-height:12.8px;color:#666}
.btn{left:122px;top:549px;width:71px;height:20px;border-radius:2px;background:linear-gradient(#f1b72c,#d5950f);color:#fff;font-family:"Hind",sans-serif;font-size:8px;font-weight:500;text-align:center;line-height:21px}
.video-frame{left:475px;top:440px;width:232px;height:158px;border:1px solid #ddd;border-radius:6px;background:#fff;box-shadow:0 1px 3px rgba(0,0,0,.1)}
.video-still{left:481px;top:446px;width:220px;height:147px;background:linear-gradient(120deg,#e9e3d8,#c9b9a8 45%,#6d4c4a 70%,#2a2224)}
.play{left:578px;top:507px;width:24px;height:24px}

.reviews{left:25px;top:626px;width:773px;height:243px;background:var(--panel);border:1px solid #ececec}
.reviews-title{left:119px;top:655px;color:#111;font-family:"Hind",sans-serif;font-size:15px;font-weight:600}
.review-img{width:83px;height:64px}
.review-title{font-size:9.5px;color:#444;font-family:"Hind",sans-serif;font-weight:500}
.review-text{width:200px;font-size:6.6px;line-height:12.4px;color:#777}
.review-time{font-size:6.8px;color:var(--orange)}

.card{background:#fff;border:1px solid #e2e2e2}
.card-head{height:29px;color:#fff;font-family:"Hind",sans-serif;font-size:12.5px;font-weight:500;padding:7px 13px 0}
.gallery-title{left:133px;top:908px;color:var(--orange);font-family:"Hind",sans-serif;font-size:15px;font-weight:400}
.thumb{width:52px;height:43px}
.feed-item{font-size:6.6px;line-height:11px;color:#888}
.feed-item b{display:block;font-weight:400;color:#444;font-size:7.4px;line-height:11px}
.feed-item i{font-style:normal;color:#555}
.feed-item a{color:var(--link-cyan);text-decoration:none}
.avatar{width:30px;height:27px;background:linear-gradient(#b58a6d,#e8d8cc)}

.site-footer{left:0;top:1132px;width:823px;height:68px;background:var(--footer)}
.footer-nav{left:121px;top:1155px;color:#fff;font-family:"Hind",sans-serif;font-weight:600;font-size:8.6px;word-spacing:1px}
.copyright{left:121px;top:1173px;color:#999;font-size:7px}
</style>
</head>
<body>

<header class="abs site-header">
  <div class="abs brand"><span class="brand-mark"></span>Glossport Drag</div>
  <div class="abs social"><span></span><span></span><span></span><span></span></div>
</header>

<nav class="abs main-nav">
  <ul>
    <li>HOME</li><li>ABOUT US</li><li>SERVICES</li><li>GALLERY</li><li>VIDEO</li><li>REVIEWS</li><li>BLOG</li><li>CONTACT</li>
  </ul>
</nav>

<section class="abs hero"></section>
<div class="abs hero-photo" role="img" aria-label="Drag queen in purple feather boa with peacock feather"></div>
<h1 class="abs hero-title">Glossport Drag Queen</h1>
<p class="abs hero-sub">Donec scelerisque leo risus</p>
<p class="abs hero-text">Vivamus porttitor purus nisi eleifend libero a tempus libero lectus feugiat felis Morbi diam mauris viverra in gravida eu mattis in ante Morbi eget arcu</p>
<div class="abs dots"><span></span><span></span><span></span><span></span></div>

<h2 class="abs intro-title">PHASELLUS FELIS DOLOR SCELERISQUE</h2>
<p class="abs intro-sub">MAURIS VEL LACUS VITAE FELIS VESTIBULUM VOL</p>
<p class="abs intro-text">Vivamus porttitor g purus nisi eleifend libero a tempus libero lectus feugiat felis Morbi diam mauris viverra in gravida eu mattis in ante Morbi eget arcu Morbi porta libero id ullamcorper nonummy nibh ligula pulvinar metus eget consectetuer augue nisi quis lacus</p>
<div class="abs btn">READ MORE</div>
<div class="abs video-frame"></div>
<div class="abs video-still" role="img" aria-label="Video still of drag performers getting ready at a dressing-room mirror"></div>
<svg class="abs play" viewBox="0 0 24 24"><circle cx="12" cy="12" r="12" fill="#1c1c1c" stroke="#fff" stroke-width="1.5"/><path d="M9.5 7.5v9l7-4.5z" fill="#fff"/></svg>

<section class="abs reviews"></section>
<h2 class="abs reviews-title">LATEST REVIEWS</h2>

<div class="abs review-img" style="left:120px;top:686px;background:linear-gradient(135deg,#7a1418,#d7b3b0 55%,#3a0c0e)" role="img" aria-label="Drag queen in white makeup and red wig"></div>
<div class="abs review-title" style="left:213px;top:685px">Duis tincidunt lectus quis</div>
<p class="abs review-text" style="left:213px;top:699px">Etiam est nunc venenatis in tristique eu imperdiet ac nisl Cum sociis natoque penatibus et magnis dis parturient montes nascetur ridiculus mus In iaculis facilisis</p>
<div class="abs review-time" style="left:213px;top:738px">2 hous ago</div>

<div class="abs review-img" style="left:422px;top:686px;background:linear-gradient(135deg,#3f7a2a,#e24fc1 50%,#5d8a3a)" role="img" aria-label="Drag performer in bright pink wig outdoors"></div>
<div class="abs review-title" style="left:517px;top:683px">Suspendisse vulputate aliquam dui</div>
<p class="abs review-text" style="left:517px;top:697px">Etiam est nunc venenatis in tristique eu imperdiet ac nisl Cum sociis natoque penatibus et magnis dis parturient montes nascetur ridiculus mus In iaculis facilisis</p>
<div class="abs review-time" style="left:517px;top:736px">2 hous ago</div>

<div class="abs review-img" style="left:119px;top:770px;background:linear-gradient(135deg,#1e1a22,#6a5a6e 50%,#2a1c2a)" role="img" aria-label="Drag performer on stage under lights"></div>
<div class="abs review-title" style="left:213px;top:767px">Morbi porta libero ullamcorper</div>
<p class="abs review-text" style="left:213px;top:781px">Etiam est nunc venenatis in tristique eu imperdiet ac nisl Cum sociis natoque penatibus et magnis dis parturient montes nascetur ridiculus mus In iaculis facilisis</p>
<div class="abs review-time" style="left:213px;top:820px">2 hous ago</div>

<div class="abs review-img" style="left:422px;top:770px;background:linear-gradient(135deg,#8e1218,#d9a48c 50%,#6e0e14)" role="img" aria-label="Two drag queens posing in front of red curtain"></div>
<div class="abs review-title" style="left:517px;top:767px">Nullam enim leo egestas</div>
<p class="abs review-text" style="left:517px;top:781px">Etiam est nunc venenatis in tristique eu imperdiet ac nisl Cum sociis natoque penatibus et magnis dis parturient montes nascetur ridiculus mus In iaculis facilisis</p>
<div class="abs review-time" style="left:517px;top:820px">2 hous ago</div>

<div class="abs card" style="left:119px;top:896px;width:188px;height:201px"></div>
<h3 class="abs gallery-title">Photo Gallery</h3>
<div class="abs thumb" style="left:133px;top:935px;background:linear-gradient(#6f8f52,#3f5a2c)" role="img" aria-label="Gallery photo of performer outdoors"></div>
<div class="abs thumb" style="left:190px;top:935px;background:linear-gradient(#c84a5a,#e3c0b0)" role="img" aria-label="Gallery photo of drag queen portrait"></div>
<div class="abs thumb" style="left:246px;top:935px;background:linear-gradient(#8e1a1e,#d8a090)" role="img" aria-label="Gallery photo of drag queen in red"></div>
<div class="abs thumb" style="left:133px;top:983px;background:linear-gradient(#6a3a8a,#c9b6d6)" role="img" aria-label="Gallery photo of masked performer in purple"></div>
<div class="abs thumb" style="left:190px;top:983px;background:linear-gradient(#3a3a3a,#cfcfcf)" role="img" aria-label="Gallery photo of skull-painted performer"></div>
<div class="abs thumb" style="left:246px;top:983px;background:linear-gradient(#e0b890,#c85a8a)" role="img" aria-label="Gallery photo of glamour makeup closeup"></div>
<div class="abs thumb" style="left:133px;top:1030px;background:linear-gradient(#8a1a3a,#e0a0a0)" role="img" aria-label="Gallery photo of two performers"></div>
<div class="abs thumb" style="left:190px;top:1030px;background:linear-gradient(#1a4a8a,#c8583a)" role="img" aria-label="Gallery photo of redhead performer"></div>
<div class="abs thumb" style="left:246px;top:1030px;background:linear-gradient(#2a2430,#c99a80)" role="img" aria-label="Gallery photo of drag queen portrait"></div>

<div class="abs card" style="left:321px;top:896px;width:181px;height:201px"></div>
<div class="abs card-head" style="left:321px;top:896px;width:181px;background:linear-gradient(#4a76bd,#2f5499)">Vombleth Feed</div>
<div class="abs avatar" style="left:332px;top:934px" role="img" aria-label="Member avatar"></div>
<div class="abs feed-item" style="left:369px;top:933px;width:128px"><b>Etiam eu urna</b>Malesuada nec ultricies sit amet porttitor mattis enim In massa libero inter<br><i>Posted 2 hours ago</i></div>
<div class="abs avatar" style="left:332px;top:988px" role="img" aria-label="Member avatar"></div>
<div class="abs feed-item" style="left:369px;top:987px;width:128px"><b>Nulla sit amet diam</b>Malesuada nec ultricies sit amet porttit-mattis enim In massa libero interdu<br><i>Posted 2 hours ago</i></div>
<div class="abs avatar" style="left:332px;top:1043px" role="img" aria-label="Member avatar"></div>
<div class="abs feed-item" style="left:369px;top:1041px;width:128px"><b>Donec convallis pede</b>Malesuada nec ultricies sit amet porttitor mattis enim In massa libero interd<br><i>Posted 2 hours ago</i></div>

<div class="abs card" style="left:521px;top:896px;width:181px;height:201px"></div>
<div class="abs card-head" style="left:521px;top:896px;width:181px;background:linear-gradient(#3fd0ef,#1fb0d8)">Flonker Feed</div>
<div class="abs feed-item" style="left:537px;top:933px;width:160px"><b>Etiam eu urna <a>@ Etiam eu urna</a></b>Malesuada nec ultricies sit amet porttitor mattis enim In massa libero interdu<br><i>Posted 2 hours ago</i></div>
<div class="abs feed-item" style="left:537px;top:986px;width:160px"><b>Donec convallis pede <a>@ Vivamus sollicitu-</a></b>Malesuada nec ultricies sit amet porttitor mattis enim In massa libero interdu<br><i>Posted 2 hours ago</i></div>
<div class="abs feed-item" style="left:537px;top:1039px;width:160px"><b>Aliquam erat <a>@ Donec scelerisque leo</a></b>Vestibulum gravida Praesent elementum elit at tellus Malesuada nec ultricies sit<br><i>Posted 2 hours ago</i></div>

<footer class="abs site-footer"></footer>
<div class="abs footer-nav">HOME | ABOUT US | SERVICES | GALLERY | VIDEO | REVIEWS | BLOG | CONTACT</div>
<div class="abs copyright">© 2014 Company Name &nbsp;All right reserved &nbsp;Term of Use</div>

</body>
</html>
```